Adapt a PowerPoint presentation to new Template

We have a new powerpoint template that we would like to adapt to our old powerpoint base presentation. I can share the old base template that is populated with information and data that needs to be adapted and "beautified" to the new template. I have all the source files necessary. Need to adapt the Lantern Holdings presentation to RBT Template. Meaning, to have the presentation look like the RBT template with no prior Lantern template scheme's (coloring, logos, font, etc)

I will be making a decision by Wednesday, October 20th, 2021

Target Market(s)

Professionals

Requirements
Must have
• Adaption to our RBT Template
Nice to have
• Fully utilized tables, graphs, and graphics
Should not have
• Any Lantern Holdings Template palate

```html
<!DOCTYPE html>
<html lang="en">
<head>
<meta charset="utf-8">
<title>RBT Quarter 2, 2021 Review</title>
<link href="https://fonts.googleapis.com/css2?family=Roboto:wght@300;400;500;700;900&display=swap" rel="stylesheet">
<style>
:root{
  --teal:#3aa0c2;
  --navy:#1c4d74;
  --blue:#1f7fb6;
  --band:#dfeef5;
  --mint:#e3f3ef;
  --foot:#4ea89e;
  --num:#2a8fc6;
  --red:#e2342f;
  --ink:#3a3a3a;
  --grey:#d9dcde;
  --paper:#eef0f1;
}
*{box-sizing:border-box;margin:0;padding:0}
html,body{width:960px;height:1200px;overflow:hidden;background:var(--paper)}
body{position:relative;font-family:'Roboto',Arial,sans-serif;color:var(--ink)}
.slide{position:absolute;width:314px;height:176px;background:#fff;overflow:hidden;box-shadow:0 1px 3px rgba(0,0,0,.18)}
.title{position:absolute;left:11px;top:10px;font-weight:700;font-size:11.5px;color:var(--navy);white-space:nowrap;letter-spacing:-.1px}
.title .lt{color:var(--teal);font-weight:500}
.logo{position:absolute;right:10px;top:10px;display:flex;align-items:center;gap:2px;font-weight:700;font-size:7.5px;color:var(--navy)}
.logo i{display:block;width:5px;height:5px;background:var(--teal)}
.foot{position:absolute;left:0;right:0;bottom:0;height:4px;background:var(--foot)}
.foot b{position:absolute;right:0;bottom:0;width:42px;height:6px;background:var(--num);color:#fff;font-size:3.5px;line-height:6px;text-align:center;clip-path:polygon(12% 0,100% 0,100% 100%,0 100%)}
.ph{position:absolute;left:0;top:0;width:314px;height:176px}

/* financial tables */
.fin{position:absolute;left:17px;top:40px;width:280px;font-size:3.2px;line-height:4.1px;color:#333}
.fin .hd,.fin .r{display:grid;grid-template-columns:36% repeat(6,1fr)}
.fin .hd{height:6px;margin-bottom:1px}
.fin .hd span{grid-column:span 2;background:var(--navy);color:#fff;font-weight:700;font-size:3.4px;line-height:6px;text-align:center;margin:0 1px}
.fin .hd span:first-child{grid-column:1;background:none}
.fin .r span{text-align:right;padding-right:2px;white-space:nowrap}
.fin .r span:first-child{text-align:left;padding-left:3px}
.fin .sec span:first-child{color:var(--teal);font-weight:700}
.fin .tot{font-weight:700}
.fin .b{background:var(--band)}
.fin .m{background:var(--mint)}
.fin .n{color:var(--red)}
.fin .net{background:var(--navy);color:#fff;font-weight:700}
.fin.one{left:30px;top:44px;width:120px}
.fin.one .hd,.fin.one .r{grid-template-columns:60% 1fr 1fr}

/* chart */
.chart{position:absolute;left:0;top:30px;width:314px;height:140px}

/* text blocks */
.h2{position:absolute;font-weight:700;font-size:11px;color:var(--navy)}
.h2 .lt{color:var(--teal);font-weight:500}
.tag{position:absolute;background:var(--blue);color:#fff;font-weight:700;font-size:4.5px;line-height:10px;padding:0 10px 0 14px;clip-path:polygon(0 0,100% 0,94% 100%,0 100%)}
.team{position:absolute;left:12px;top:115px;list-style:none;font-size:6.4px;line-height:11.5px;font-weight:700;color:#333}
.team li::before{content:"•";margin-right:5px}
.team em{font-style:normal;font-weight:400;font-size:4.6px;color:var(--teal)}
.focus{position:absolute;height:30px;background:var(--blue);color:#fff;display:flex;align-items:center;gap:8px;padding-left:14px;clip-path:polygon(6% 0,100% 0,94% 100%,0 100%)}
.focus b{font-size:15px;font-weight:700}
.focus span{font-size:5.3px;line-height:6.5px}
.stack{position:absolute;left:0;top:48px;width:104px;height:111px;background:var(--blue);clip-path:polygon(0 0,100% 0,82% 100%,0 100%);color:#fff}
.stack div{position:absolute;left:10px;display:flex;gap:5px;align-items:center}
.stack b{font-size:9.5px}
.stack span{font-size:4px;line-height:4.8px;width:60px}
.head{position:absolute;width:38px;height:38px}
.who{position:absolute;width:60px;text-align:center;font-size:4.6px;font-weight:700;color:#333;line-height:5px}
.who em{display:block;font-style:normal;font-weight:400;font-size:3px;color:var(--teal)}

/* cash flow */
.cf{position:absolute;left:3px;top:30px;width:308px;font-size:2.6px;line-height:7.1px;color:#444}
.cf .r{display:grid;grid-template-columns:38px repeat(13,1fr)}
.cf .r span{text-align:right;padding-right:1px;white-space:nowrap}
.cf .r span:first-child{text-align:left;color:var(--teal)}
.cf .hd{background:var(--navy);color:#fff;font-weight:700}
.cf .hd span:first-child{color:#fff}
.cf .b{background:var(--band)}
.cf .net{background:var(--navy);color:#fff;font-weight:700}
.cf .net span:first-child{color:#fff}
.cf .cap{text-align:center;font-weight:700;font-size:3.2px;line-height:6px;color:#222}
.note{position:absolute;left:123px;top:73px;width:108px;height:15px;background:#fff;color:var(--blue);font-size:3.6px;font-weight:700;text-align:center;line-height:15px;box-shadow:0 0 2px rgba(0,0,0,.1)}

.body{position:absolute;font-size:4.6px;line-height:7px;color:#444}
.body .sub{font-weight:700;color:var(--blue);font-size:5.4px}
.body ul{list-style:none}
.body li::before{content:"•";margin-right:4px;color:#666}
.body .in{padding-left:10px}
.body .in::before{content:"✓";color:#666}
.big{position:absolute;font-size:13.5px;font-weight:500;color:var(--teal)}
.facts{position:absolute;list-style:none;font-size:5.4px;line-height:15px;color:#444}
.facts li::before{content:"•";margin-right:6px}
.facts b{color:var(--teal);font-weight:700;font-size:6.2px}
.caption{position:absolute;font-weight:700;font-size:4.6px;color:#fff}
.mini{position:absolute;font-size:4.6px;line-height:8.7px;color:#444;list-style:none}
.mini li::before{content:"•";margin-right:4px}
.mini b{color:var(--blue)}
.lead{position:absolute;font-size:5.5px;font-weight:700;color:var(--blue)}
.lead.dark{color:#333}
.banner{position:absolute;background:var(--blue);color:#fff;font-size:4.8px;font-weight:700;line-height:11px;padding-left:6px;clip-path:polygon(0 0,100% 0,96% 100%,0 100%)}
.colhead{position:absolute;font-size:5.4px;font-weight:700;color:var(--blue);text-decoration:underline}
.partner{position:absolute;left:30px;top:78px;display:flex;align-items:center;gap:8px}
.partner i{display:block;width:30px;height:34px;background:#e8a33a}
.partner span{font-size:8.5px;line-height:10px;letter-spacing:2.5px;color:#8a96a3;font-weight:400}
.checks{position:absolute;left:156px;top:60px;list-style:none;font-size:4.8px;line-height:11px;color:#333}
.checks li{display:flex;align-items:center;gap:5px}
.checks svg{width:6px;height:6px}
.cal{position:absolute;font-size:4px;line-height:5.5px;color:#444}
.cal b{display:block;font-size:4.6px;color:#333}
.cal b.t{color:var(--blue)}
.fl{position:absolute;left:160px;top:59px;width:103px;height:76px;background:var(--blue);color:#fff;padding:8px 0 0 14px;font-size:5.5px;line-height:6.4px;font-weight:700;clip-path:polygon(4% 0,100% 0,100% 100%,0 100%)}
.fl em{display:block;font-weight:400;font-style:italic;margin-bottom:5px}
.qbox{position:absolute;left:32px;top:26px;width:250px;height:124px;background:rgba(31,127,182,.93);color:#fff;text-align:center}
.qbox .mark{position:absolute;left:0;right:0;top:44px;font-size:8px;font-weight:700}
.qbox .q{position:absolute;left:0;right:0;top:64px;font-size:18px;font-weight:700}
</style>
</head>
<body>

<!-- 1 cover -->
<section class="slide" style="left:3px;top:12px">
  <svg class="ph" viewBox="0 0 314 176" role="img" aria-label="Teal-toned photo of a mountain highway">
    <defs><linearGradient id="gc" x1="0" y1="0" x2="1" y2="1"><stop offset="0" stop-color="#3c9fbf"/><stop offset=".6" stop-color="#2b8db0"/><stop offset="1" stop-color="#1f7096"/></linearGradient></defs>
    <rect width="314" height="176" fill="url(#gc)"/>
  </svg>
  <div style="position:absolute;left:136px;top:70px;color:#fff;font-size:25px;font-weight:700">RBT</div>
  <div style="position:absolute;left:136px;top:103px;color:#fff;font-size:7.5px;font-weight:300">Quarter 2, 2021</div>
</section>

<!-- 2 qtr actual vs budget -->
<section class="slide" style="left:323px;top:12px">
  <h1 class="title"><span class="lt">Qtr. Actual</span> vs Budget</h1>
  <div class="logo"><i></i>RBT</div>
  <div class="fin" style="top:32px">
    <div class="hd"><span></span><span>Actual</span><span>Budget</span><span>Variance B/(W)</span></div>
    <div class="r sec b"><span>Sales</span></div>
    <div class="r b"><span>Sales</span><span>4,479,434</span><span>100.00%</span><span>3,606,189</span><span>100.00%</span><span>873,245</span><span>24.22%</span></div>
    <div class="r tot b"><span>Total Sales</span><span>4,479,434</span><span>100.00%</span><span>3,606,189</span><span>100.00%</span><span>873,245</span><span>24.22%</span></div>
    <div class="r sec"><span>Prime Cost</span></div>
    <div class="r"><span>Cost of Sales</span><span>1,273,991</span><span>28.44%</span><span>1,073,583</span><span>29.77%</span><span class="n">-200,408</span><span class="n">-18.67%</span></div>
    <div class="r"><span>Personnel Costs</span><span>1,344,279</span><span>30.01%</span><span>1,045,234</span><span>28.98%</span><span class="n">-299,045</span><span class="n">-28.61%</span></div>
    <div class="r tot"><span>Total Prime Cost</span><span>2,618,271</span><span>58.45%</span><span>2,118,817</span><span>58.76%</span><span class="n">-499,454</span><span class="n">-23.57%</span></div>
    <div class="r sec"><span>Operating Expense</span></div>
    <div class="r tot"><span>Restaurant Controllable Profit</span><span>1,709,704</span><span>38.17%</span><span>1,365,221</span><span>37.86%</span><span>344,544</span><span>25.24%</span></div>
    <div class="r"><span>Controllable Expenses</span><span>455,363</span><span>10.17%</span><span>357,436</span><span>9.91%</span><span class="n">-97,926</span><span class="n">-27.4%</span></div>
    <div class="r"><span>3rd Party Delivery Fees</span><span>38,096</span><span>0.85%</span><span></span><span></span><span class="n">-38,096</span><span>0.0%</span></div>
    <div class="r"><span>Advertising</span><span>22,338</span><span>0.50%</span><span>16,024</span><span>0.44%</span><span class="n">-6,314</span><span class="n">-39.4%</span></div>
    <div class="r"><span>Other Expense</span><span>595</span><span>0.01%</span><span>9,015</span><span>0.25%</span><span>8,420</span><span>93.4%</span></div>
    <div class="r tot"><span>Total Operating Expense</span><span>516,392</span><span>11.53%</span><span>382,477</span><span>10.61%</span><span class="n">-133,915</span><span class="n">-35.01%</span></div>
    <div class="r sec b"><span>Non Controllable Expense</span></div>
    <div class="r b"><span>Non-Controllable Expenses</span><span>770,085</span><span>17.19%</span><span>712,459</span><span>19.76%</span><span class="n">-57,626</span><span class="n">-8.09%</span></div>
    <div class="r tot b"><span>Total Non Controllable Expense</span><span>770,085</span><span>17.19%</span><span>712,459</span><span>19.76%</span><span class="n">-57,626</span><span class="n">-8.09%</span></div>
    <div class="r tot b"><span>Total Field Contribution</span><span>574,607</span><span>12.83%</span><span>392,430</span><span>10.88%</span><span>182,251</span><span>46.44%</span></div>
    <div class="r sec m"><span>Corporate Overhead &amp; Other</span></div>
    <div class="r m"><span>Interest Income</span><span></span><span></span><span>131</span><span>0.00%</span><span>131</span><span>100.0%</span></div>
    <div class="r m"><span>Other Income</span><span>-23</span><span>0.00%</span><span>31,651</span><span>0.88%</span><span>31,674</span><span>100.07%</span></div>
    <div class="r m"><span>Amortization</span><span></span><span></span><span></span><span></span><span></span><span>0.0%</span></div>
    <div class="r m"><span>Depreciation</span><span></span><span></span><span>167,310</span><span>4.64%</span><span>167,310</span><span>100.0%</span></div>
    <div class="r tot m"><span>Total Corporate Overhead &amp; Other</span><span>-23</span><span>0.00%</span><span>199,092</span><span>5.52%</span><span>199,115</span><span>100.01%</span></div>
    <div class="r net"><span>Net Profit</span><span>574,709</span><span>12.83%</span><span>193,344</span><span>5.36%</span><span>381,365</span><span>197.25%</span></div>
  </div>
  <div class="foot"><b>2</b></div>
</section>

<!-- 3 qtr actual vs prior year -->
<section class="slide" style="left:643px;top:12px">
  <svg class="ph" viewBox="0 0 314 176" role="img" aria-label="Photo of a wooden block corner on a pale teal surface">
    <defs><linearGradient id="gw" x1="0" y1="0" x2="1" y2="1"><stop offset="0" stop-color="#e6c79a"/><stop offset="1" stop-color="#c69b64"/></linearGradient>
    <linearGradient id="gt" x1="0" y1="0" x2="0" y2="1"><stop offset="0" stop-color="#bfe7ee"/><stop offset="1" stop-color="#e9f7f8"/></linearGradient></defs>
    <polygon points="230,0 314,0 314,176 250,176" fill="url(#gt)"/>
    <polygon points="245,0 314,0 314,60" fill="url(#gw)"/>
  </svg>
  <h1 class="title"><span class="lt">Qtr. Actual</span> vs Prior Year</h1>
  <div class="fin" style="top:38px;left:16px;width:238px">
    <div class="hd"><span></span><span>Actual</span><span>Prior Year</span><span>Variance B/(W)</span></div>
    <div class="r sec b"><span>Sales</span></div>
    <div class="r b"><span>Sales</span><span>4,479,434</span><span>100.00%</span><span>3,080,292</span><span>100.00%</span><span>1,399,142</span><span>45.42%</span></div>
    <div class="r tot b"><span>Total Sales</span><span>4,479,434</span><span>100.00%</span><span>3,080,292</span><span>100.00%</span><span>1,399,142</span><span>45.42%</span></div>
    <div class="r sec"><span>Prime Cost</span></div>
    <div class="r"><span>Cost of Sales</span><span>1,273,991</span><span>28.44%</span><span>900,506</span><span>29.23%</span><span class="n">-373,486</span><span class="n">-41.48%</span></div>
    <div class="r"><span>Personnel Costs</span><span>1,344,279</span><span>30.01%</span><span>1,014,534</span><span>32.94%</span><span class="n">-329,745</span><span class="n">-32.5%</span></div>
    <div class="r tot"><span>Total Prime Cost</span><span>2,618,271</span><span>58.45%</span><span>1,915,040</span><span>62.17%</span><span class="n">-703,231</span><span class="n">-36.72%</span></div>
    <div class="r sec"><span>Operating Expense</span></div>
    <div class="r tot"><span>Restaurant Controllable Profit</span><span>1,709,704</span><span>38.17%</span><span>1,059,840</span><span>34.38%</span><span>640,925</span><span>61.48%</span></div>
    <div class="r"><span>Controllable Expenses</span><span>455,363</span><span>10.17%</span><span>304,424</span><span>9.88%</span><span class="n">-150,939</span><span class="n">-49.58%</span></div>
    <div class="r"><span>3rd Party Delivery Fees</span><span>38,096</span><span>0.85%</span><span>75,618</span><span>2.45%</span><span>37,523</span><span>49.62%</span></div>
    <div class="r"><span>Advertising</span><span>22,338</span><span>0.50%</span><span>28,675</span><span>0.93%</span><span>6,337</span><span>22.1%</span></div>
    <div class="r"><span>Other Expense</span><span>595</span><span>0.01%</span><span></span><span></span><span class="n">-595</span><span>0.0%</span></div>
    <div class="r tot"><span>Total Operating Expense</span><span>516,392</span><span>11.53%</span><span>408,718</span><span>13.27%</span><span class="n">-107,675</span><span class="n">-26.34%</span></div>
    <div class="r sec b"><span>Non Controllable Expense</span></div>
    <div class="r b"><span>Non-Controllable Expenses</span><span>770,085</span><span>17.19%</span><span>580,453</span><span>18.84%</span><span class="n">-189,632</span><span class="n">-32.67%</span></div>
    <div class="r tot b"><span>Total Non Controllable Expense</span><span>770,085</span><span>17.19%</span><span>580,453</span><span>18.84%</span><span class="n">-189,632</span><span class="n">-32.67%</span></div>
    <div class="r tot b"><span>Total Field Contribution</span><span>574,607</span><span>12.83%</span><span>176,061</span><span>5.72%</span><span>398,605</span><span>226.38%</span></div>
    <div class="r sec m"><span>Corporate Overhead &amp; Other</span></div>
    <div class="r m"><span>Interest Income</span><span></span><span></span><span>-219</span><span>-0.01%</span><span>-219</span><span>100.0%</span></div>
    <div class="r m"><span>Other Income</span><span>-23</span><span>0.00%</span><span>-14,417</span><span>-0.47%</span><span>-14,394</span><span>99.84%</span></div>
    <div class="r m"><span>Amortization</span><span></span><span></span><span>15,813</span><span>0.51%</span><span>15,813</span><span>100.0%</span></div>
    <div class="r m"><span>Depreciation</span><span></span><span></span><span>121,142</span><span>3.93%</span><span>121,142</span><span>100.0%</span></div>
    <div class="r tot m"><span>Total Corporate Overhead &amp; Other</span><span>-23</span><span>0.00%</span><span>122,319</span><span>3.97%</span><span>122,342</span><span>100.02%</span></div>
    <div class="r net"><span>Net Profit</span><span>574,709</span><span>12.83%</span><span>53,762</span><span>1.75%</span><span>520,947</span><span>968.99%</span></div>
  </div>
</section>

<!-- 4 ytd vs budget -->
<section class="slide" style="left:3px;top:212px">
  <h1 class="title"><span class="lt">YTD Actual</span> vs. Budget</h1>
  <div class="logo"><i></i>RBT</div>
  <div class="fin" style="top:44px;left:25px;width:268px">
    <div class="hd"><span></span><span>YTD Actual</span><span>YTD Budget</span><span>Variance B/(W)</span></div>
    <div class="r sec b"><span>Sales</span></div>
    <div class="r b"><span>Sales</span><span>8,198,831</span><span>100.00%</span><span>6,972,938</span><span>100.00%</span><span>1,225,893</span><span>17.58%</span></div>
    <div class="r tot b"><span>Total Sales</span><span>8,198,831</span><span>100.00%</span><span>6,972,938</span><span>100.00%</span><span>1,225,893</span><span>17.58%</span></div>
    <div class="r sec"><span>Prime Cost</span></div>
    <div class="r"><span>Cost of Sales</span><span>2,320,254</span><span>28.30%</span><span>2,075,847</span><span>29.77%</span><span class="n">-244,407</span><span class="n">-11.77%</span></div>
    <div class="r"><span>Personnel Costs</span><span>2,443,603</span><span>29.80%</span><span>2,021,668</span><span>28.99%</span><span class="n">-421,936</span><span class="n">-20.87%</span></div>
    <div class="r tot"><span>Total Prime Cost</span><span>4,763,858</span><span>58.10%</span><span>4,097,515</span><span>58.76%</span><span class="n">-666,343</span><span class="n">-16.26%</span></div>
    <div class="r sec"><span>Operating Expense</span></div>
    <div class="r tot"><span>Restaurant Controllable Profit</span><span>3,131,047</span><span>38.19%</span><span>2,630,280</span><span>37.65%</span><span>401,767</span><span>18.63%</span></div>
    <div class="r"><span>Controllable Expenses</span><span>858,531</span><span>10.47%</span><span>690,919</span><span>9.91%</span><span class="n">-167,612</span><span class="n">-24.26%</span></div>
    <div class="r"><span>3rd Party Delivery Fees</span><span>73,071</span><span>0.89%</span><span></span><span></span><span class="n">-73,071</span><span>0.0%</span></div>
    <div class="r"><span>Advertising</span><span>39,296</span><span>0.48%</span><span>30,988</span><span>0.44%</span><span class="n">-8,308</span><span class="n">-26.81%</span></div>
    <div class="r"><span>Other Expense</span><span>1,521</span><span>0.02%</span><span>17,432</span><span>0.25%</span><span>15,911</span><span>91.27%</span></div>
    <div class="r tot"><span>Total Operating Expense</span><span>972,420</span><span>11.86%</span><span>739,340</span><span>10.60%</span><span class="n">-233,081</span><span class="n">-31.53%</span></div>
    <div class="r sec b"><span>Non Controllable Expense</span></div>
    <div class="r b"><span>Non-Controllable Expenses</span><span>1,464,602</span><span>17.87%</span><span>1,394,933</span><span>20.01%</span><span class="n">-69,670</span><span class="n">-5.01%</span></div>
    <div class="r tot b"><span>Total Non Controllable Expense</span><span>1,464,602</span><span>17.87%</span><span>1,394,933</span><span>20.01%</span><span class="n">-69,670</span><span class="n">-5.01%</span></div>
    <div class="r tot b"><span>Total Field Contribution</span><span>997,750</span><span>12.17%</span><span>741,180</span><span>10.63%</span><span>256,600</span><span>34.62%</span></div>
    <div class="r sec m"><span>Corporate Overhead &amp; Other</span></div>
    <div class="r m"><span>Interest Income</span><span></span><span></span><span>249</span><span>0.00%</span><span>249</span><span>100.0%</span></div>
    <div class="r m"><span>Other Income</span><span>8,389</span><span>0.10%</span><span>61,125</span><span>0.88%</span><span>52,737</span><span>86.28%</span></div>
    <div class="r m"><span>Amortization</span><span></span><span></span><span></span><span></span><span></span><span>0.0%</span></div>
    <div class="r m"><span>Depreciation</span><span></span><span></span><span>325,311</span><span>4.67%</span><span>325,311</span><span>100.0%</span></div>
    <div class="r tot m"><span>Total Corporate Overhead &amp; Other</span><span>8,389</span><span>0.10%</span><span>386,685</span><span>5.55%</span><span>378,296</span><span>97.83%</span></div>
    <div class="r net"><span>Net Profit</span><span>989,361</span><span>12.07%</span><span>354,465</span><span>5.08%</span><span>634,896</span><span>179.11%</span></div>
  </div>
  <div class="foot"><b>4</b></div>
</section>

<!-- 5 ytd vs prior -->
<section class="slide" style="left:323px;top:212px">
  <h1 class="title"><span class="lt">YTD Actual</span> vs. Prior</h1>
  <div class="logo"><i></i>RBT</div>
  <div class="fin" style="top:44px;left:22px;width:270px">
    <div class="hd"><span></span><span>YTD Actual</span><span>YTD Prior</span><span>Variance B/(W)</span></div>
    <div class="r sec b"><span>Sales</span></div>
    <div class="r b"><span>Sales</span><span>8,198,831</span><span>100.00%</span><span>6,067,126</span><span>100.00%</span><span>2,131,704</span><span>35.14%</span></div>
    <div class="r tot b"><span>Total Sales</span><span>8,198,831</span><span>100.00%</span><span>6,067,126</span><span>100.00%</span><span>2,131,704</span><span>35.14%</span></div>
    <div class="r sec"><span>Prime Cost</span></div>
    <div class="r"><span>Cost of Sales</span><span>2,320,254</span><span>28.30%</span><span>1,814,850</span><span>29.91%</span><span class="n">-505,405</span><span class="n">-27.85%</span></div>
    <div class="r"><span>Personnel Costs</span><span>2,443,603</span><span>29.80%</span><span>1,939,996</span><span>31.98%</span><span class="n">-503,607</span><span class="n">-25.96%</span></div>
    <div class="r tot"><span>Total Prime Cost</span><span>4,763,858</span><span>58.10%</span><span>3,754,846</span><span>61.89%</span><span class="n">-1,009,012</span><span class="n">-26.87%</span></div>
    <div class="r sec"><span>Operating Expense</span></div>
    <div class="r tot"><span>Restaurant Controllable Profit</span><span>3,131,047</span><span>38.19%</span><span>2,110,217</span><span>34.78%</span><span>1,020,830</span><span>48.38%</span></div>
    <div class="r"><span>Controllable Expenses</span><span>858,531</span><span>10.47%</span><span>621,958</span><span>10.25%</span><span class="n">-236,573</span><span class="n">-38.04%</span></div>
    <div class="r"><span>3rd Party Delivery Fees</span><span>73,071</span><span>0.89%</span><span>75,618</span><span>1.25%</span><span>2,547</span><span>3.37%</span></div>
    <div class="r"><span>Advertising</span><span>39,296</span><span>0.48%</span><span>55,592</span><span>0.92%</span><span>16,296</span><span>29.31%</span></div>
    <div class="r"><span>Other Expense</span><span>1,521</span><span>0.02%</span><span></span><span></span><span class="n">-1,521</span><span>0.0%</span></div>
    <div class="r tot"><span>Total Operating Expense</span><span>972,420</span><span>11.86%</span><span>753,169</span><span>12.41%</span><span class="n">-219,252</span><span class="n">-29.11%</span></div>
    <div class="r sec b"><span>Non Controllable Expense</span></div>
    <div class="r b"><span>Non-Controllable Expenses</span><span>1,464,602</span><span>17.87%</span><span>1,224,136</span><span>20.18%</span><span class="n">-240,467</span><span class="n">-19.66%</span></div>
    <div class="r tot b"><span>Total Non Controllable Expense</span><span>1,464,602</span><span>17.87%</span><span>1,224,136</span><span>20.18%</span><span class="n">-240,467</span><span class="n">-19.66%</span></div>
    <div class="r tot b"><span>Total Field Contribution</span><span>997,750</span><span>12.17%</span><span>334,977</span><span>5.52%</span><span>662,773</span><span>197.86%</span></div>
    <div class="r sec m"><span>Corporate Overhead &amp; Other</span></div>
    <div class="r m"><span>Interest Income</span><span></span><span></span><span>-294</span><span>-0.01%</span><span class="n">-294</span><span>100.0%</span></div>
    <div class="r m"><span>Other Income</span><span>8,389</span><span>0.10%</span><span>-40,535</span><span>-0.67%</span><span class="n">-48,923</span><span>120.7%</span></div>
    <div class="r m"><span>Amortization</span><span></span><span></span><span>31,636</span><span>0.52%</span><span>31,636</span><span>100.0%</span></div>
    <div class="r m"><span>Depreciation</span><span></span><span></span><span>241,928</span><span>3.99%</span><span>241,928</span><span>100.0%</span></div>
    <div class="r tot m"><span>Total Corporate Overhead &amp; Other</span><span>8,389</span><span>0.10%</span><span>232,735</span><span>3.84%</span><span>224,346</span><span>96.4%</span></div>
    <div class="r net"><span>Net Profit</span><span>989,361</span><span>12.07%</span><span>102,242</span><span>1.69%</span><span>887,119</span><span>867.66%</span></div>
  </div>
  <div class="foot"><b>5</b></div>
</section>

<!-- 6 chart -->
<section class="slide" style="left:643px;top:212px">
  <h1 class="title"><span class="lt">YTD Actual</span> vs. Projected Cash</h1>
  <div class="logo"><i></i>RBT</div>
  <svg class="chart" viewBox="0 30 314 140" font-family="Roboto, sans-serif" font-size="3.6" fill="#333">
    <g stroke="#e4e4e4" stroke-width=".4">
      <line x1="52" y1="48" x2="300" y2="48"/><line x1="52" y1="63.3" x2="300" y2="63.3"/><line x1="52" y1="78.7" x2="300" y2="78.7"/><line x1="52" y1="94" x2="300" y2="94"/><line x1="52" y1="109.3" x2="300" y2="109.3"/><line x1="52" y1="124.7" x2="300" y2="124.7"/><line x1="52" y1="140" x2="300" y2="140"/>
    </g>
    <g text-anchor="end">
      <text x="48" y="49.2">$1,500,000</text><text x="48" y="64.5">$1,400,000</text><text x="48" y="79.9">$1,300,000</text><text x="48" y="95.2">$1,200,000</text><text x="48" y="110.5">$1,100,000</text><text x="48" y="125.9">$1,000,000</text><text x="48" y="141.2">$900,000</text>
    </g>
    <text x="22" y="96" transform="rotate(-90 22 96)" text-anchor="middle">Dollars</text>
    <polyline points="70,102.7 106,104.5 142,95.9 178,86.3 214,77.7 250,68.2 286,104.9" fill="none" stroke="#1f6f9e" stroke-width="1.1"/>
    <polyline points="70,121.8 106,126 142,108.7 178,84.3 214,88.7 250,63.6 286,47.7" fill="none" stroke="#3a9aa0" stroke-width="1.1"/>
    <g fill="#fff" stroke="#1f6f9e" stroke-width=".6">
      <circle cx="70" cy="102.7" r="1"/><circle cx="106" cy="104.5" r="1"/><circle cx="142" cy="95.9" r="1"/><circle cx="178" cy="86.3" r="1"/><circle cx="214" cy="77.7" r="1"/><circle cx="250" cy="68.2" r="1"/><circle cx="286" cy="104.9" r="1"/>
    </g>
    <g fill="#fff" stroke="#3a9aa0" stroke-width=".6">
      <circle cx="70" cy="121.8" r="1"/><circle cx="106" cy="126" r="1"/><circle cx="142" cy="108.7" r="1"/><circle cx="178" cy="84.3" r="1"/><circle cx="214" cy="88.7" r="1"/><circle cx="250" cy="63.6" r="1"/><circle cx="286" cy="47.7" r="1"/>
    </g>
    <g text-anchor="middle">
      <text x="70" y="146">P1</text><text x="106" y="146">P2</text><text x="142" y="146">P3</text><text x="178" y="146">P4</text><text x="214" y="146">P5</text><text x="250" y="146">P6</text><text x="286" y="146">P7</text>
      <text x="70" y="152">$1,143,090</text><text x="106" y="152">$1,131,558</text><text x="142" y="152">$1,187,848</text><text x="178" y="152">$1,250,190</text><text x="214" y="152">$1,306,052</text><text x="250" y="152">$1,368,051</text><text x="286" y="152">$1,128,802</text>
      <text x="70" y="158">$1,018,795</text><text x="106" y="158">$991,213</text><text x="142" y="158">$1,104,349</text><text x="178" y="158">$1,263,020</text><text x="214" y="158">$1,234,562</text><text x="250" y="158">$1,398,062</text><text x="286" y="158">$1,501,718</text>
    </g>
    <line x1="22" y1="151" x2="30" y2="151" stroke="#1f6f9e" stroke-width="1"/><text x="31" y="152.2">Cash Projection</text>
    <line x1="22" y1="157" x2="30" y2="157" stroke="#3a9aa0" stroke-width="1"/><text x="31" y="158.2">Cash Balance</text>
  </svg>
  <div class="foot"><b>6</b></div>
</section>

<!-- 7 qtr 3 budget -->
<section class="slide" style="left:3px;top:412px">
  <svg class="ph" viewBox="0 0 314 176" role="img" aria-label="Grey photo of paper boats on a wooden table, one in blue">
    <defs><linearGradient id="gb" x1="0" y1="0" x2="1" y2="1"><stop offset="0" stop-color="#c9cccd"/><stop offset=".55" stop-color="#8e9393"/><stop offset="1" stop-color="#5d6365"/></linearGradient></defs>
    <polygon points="235,0 314,0 314,176 145,176" fill="url(#gb)"/>
    <ellipse cx="252" cy="118" rx="22" ry="18" fill="#4eb1cf" opacity=".8"/>
  </svg>
  <div class="logo" style="left:12px;right:auto"><i></i>RBT</div>
  <h1 class="title" style="left:42px">Qtr. <span class="lt" style="font-weight:700">3</span> - 21 Budget</h1>
  <div class="fin one" style="left:52px;width:176px;top:42px">
    <div class="hd" style="grid-template-columns:60% 1fr"><span style="grid-column:1"></span><span style="grid-column:2">Total</span></div>
    <div class="r sec b"><span>Sales</span></div>
    <div class="r b"><span>Sales</span><span>3,587,383</span><span>100.00%</span></div>
    <div class="r tot b"><span>Total Sales</span><span>3,587,383</span><span>100.00%</span></div>
    <div class="r sec"><span>Prime Cost</span></div>
    <div class="r"><span>Cost of Sales</span><span>1,067,932</span><span>29.77%</span></div>
    <div class="r"><span>Personnel Costs</span><span>1,039,704</span><span>28.98%</span></div>
    <div class="r tot"><span>Total Prime Cost</span><span>2,107,636</span><span>58.75%</span></div>
    <div class="r sec"><span>Operating Expense</span></div>
    <div class="r tot"><span>Restaurant Controllable Profit</span><span>1,357,871</span><span>37.85%</span></div>
    <div class="r"><span>Controllable Expenses</span><span>357,681</span><span>9.97%</span></div>
    <div class="r"><span>Advertising</span><span>15,911</span><span>0.44%</span></div>
    <div class="r"><span>Other Expense</span><span>8,968</span><span>0.25%</span></div>
    <div class="r tot"><span>Total Operating Expense</span><span>382,561</span><span>10.66%</span></div>
    <div class="r sec b"><span>Non Controllable Expense</span></div>
    <div class="r b"><span>Non-Controllable Expenses</span><span>711,768</span><span>19.84%</span></div>
    <div class="r tot b"><span>Total Non Controllable Expense</span><span>711,768</span><span>19.84%</span></div>
    <div class="r tot b"><span>Total Field Contribution</span><span>385,418</span><span>10.74%</span></div>
    <div class="r sec m"><span>Corporate Overhead &amp; Other</span></div>
    <div class="r m"><span>Interest Income</span><span>129</span><span>0.00%</span></div>
    <div class="r m"><span>Other Income</span><span>31,480</span><span>0.88%</span></div>
    <div class="r m"><span>Depreciation</span><span>166,738</span><span>4.65%</span></div>
    <div class="r tot m"><span>Total Corporate Overhead &amp; Other</span><span>198,347</span><span>5.53%</span></div>
    <div class="r net"><span>Net Profit</span><span>187,071</span><span>5.21%</span></div>
  </div>
</section>

<!-- 8 go forward step plan -->
<section class="slide" style="left:323px;top:412px">
  <svg class="ph" viewBox="0 0 314 176" role="img" aria-label="Photo of a coastal road at sunset">
    <defs><linearGradient id="gr" x1="0" y1="0" x2="0" y2="1"><stop offset="0" stop-color="#4d6f8c"/><stop offset=".45" stop-color="#e5a866"/><stop offset="1" stop-color="#3c3a3a"/></linearGradient></defs>
    <polygon points="235,0 314,0 314,176 130,176" fill="url(#gr)"/>
  </svg>
  <div class="logo" style="left:12px;right:auto"><i></i>RBT</div>
  <h2 class="h2" style="left:15px;top:42px"><span class="lt" style="font-weight:700">Go Forward</span> Step Plan</h2>
  <div class="tag" style="left:0;top:77px">RBT Support Team</div>
  <ul class="team" style="top:94px;font-size:6.2px;line-height:11.8px">
    <li>Mark Halvorsen, <em>CEO</em></li>
    <li>Ben Castell, <em>COO</em></li>
    <li>Julia Renner,<em>Controller</em></li>
    <li>Claire Dunmore, <em>Human Relations</em></li>
    <li>Owen Pratt, <em>Operations Services Manager</em></li>
  </ul>
  <div class="tag" style="left:161px;top:39px;background:#3f9fa6">Key Focus Items</div>
  <div class="focus" style="left:152px;top:55px;width:132px"><b>01</b><span>Bench building process<br>followed for people growth.</span></div>
  <div class="focus" style="left:142px;top:95px;width:140px"><b>02</b><span>Review CapX projects for year end.</span></div>
  <div class="focus" style="left:132px;top:135px;width:140px"><b>03</b><span>Prepare NRO management<br>team for Sandhill and Falcon</span></div>
</section>

<!-- 9 step plan people -->
<section class="slide" style="left:643px;top:412px">
  <h1 class="title" style="top:10px"><span class="lt" style="font-weight:700">Go Forward</span> Step Plan</h1>
  <div class="logo"><i></i>RBT</div>
  <div class="stack">
    <div style="top:20px"><b>01</b><span>Bench building process followed for people growth.</span></div>
    <div style="top:46px"><b>02</b><span>Review CapX projects for year end.</span></div>
    <div style="top:72px"><b>03</b><span>Prepare NRO management team for Sandhill and Falcon</span></div>
  </div>
  <div class="head" role="img" aria-label="Portrait photo placeholder" style="left:119px;top:46px;background:linear-gradient(#e4e4e4,#9a9a9a)"></div>
  <div class="head" role="img" aria-label="Portrait photo placeholder" style="left:183px;top:46px;background:linear-gradient(#e4e4e4,#8d8d8d)"></div>
  <div class="head" role="img" aria-label="Portrait photo placeholder" style="left:247px;top:46px;background:linear-gradient(#eaeaea,#a2a2a2)"></div>
  <div class="who" style="left:108px;top:87px">Mark Halvorsen,<em>CEO</em></div>
  <div class="who" style="left:172px;top:87px">Ben Castell,<em>COO</em></div>
  <div class="who" style="left:236px;top:87px">Julia Renner,<em>Controller</em></div>
  <div class="head" role="img" aria-label="Portrait photo placeholder" style="left:119px;top:106px;background:var(--grey)"></div>
  <div class="head" role="img" aria-label="Portrait photo placeholder" style="left:183px;top:106px;background:var(--grey)"></div>
  <div class="who" style="left:108px;top:146px">Claire Dunmore,<em>Human Relations</em></div>
  <div class="who" style="left:172px;top:146px">Owen Pratt,<em>Operations Services Manager</em></div>
  <div class="foot"><b>9</b></div>
</section>

<!-- 10 cash flow model -->
<section class="slide" style="left:3px;top:612px">
  <h1 class="title"><span class="lt">2021 Updated</span> Cash Flow Model</h1>
  <div class="logo"><i></i>RBT</div>
  <div class="cf" style="top:28px">
    <div class="cap">OPTIMISTIC PROJECTION</div>
    <div class="r hd" style="line-height:5px"><span></span><span>P1 2021</span><span>P2 2021</span><span>P3 2021</span><span>P4 2021</span><span>P5 2021</span><span>P6 2021</span><span>P7 2021</span><span>P8 2021</span><span>P9 2021</span><span>P10 2021</span><span>P11 2021</span><span>P12 2021</span><span>P13 2021</span></div>
    <div class="r b"><span>Cash, Beginning of Period</span><span></span><span></span><span></span><span></span><span>$1,229,940</span><span>$1,296,340</span><span>$1,374,465</span><span>$1,454,673</span><span>$1,537,415</span><span>$1,616,551</span><span>$1,719,569</span><span>$1,775,327</span><span>$1,801,176</span></div>
    <div class="r"><span>Cash Flow from Operations</span><span></span><span></span><span></span><span></span><span>$169,574</span><span>$181,285</span><span>$183,409</span><span>$185,922</span><span>$176,316</span><span>$174,018</span><span>$170,758</span><span>$166,643</span><span>$170,927</span></div>
    <div class="r"><span>Cap Ex &amp; Other</span></div>
    <div class="r"><span>Sandhill Development</span><span></span><span></span><span></span><span></span><span></span><span></span><span></span><span></span><span></span><span>$25,000</span><span>$60,000</span><span>$60,000</span><span>$32,000</span></div>
    <div class="r"><span>Falcon Marketplace</span><span></span><span></span><span></span><span></span><span></span><span></span><span></span><span></span><span></span><span></span><span>$25,000</span><span>$60,000</span><span>$60,000</span></div>
    <div class="r b"><span></span><span>$ -</span><span>$ -</span><span>$ -</span><span>$ -</span><span>$ -</span><span>$ -</span><span>$ -</span><span>$ -</span><span>$ -</span><span>25,000</span><span>75,000</span><span>100,000</span><span>92,000</span></div>
    <div class="r"><span>Debt Payments</span></div>
    <div class="r"><span>Lender A</span><span></span><span></span><span></span><span></span><span>3,940</span><span>3,940</span><span>3,940</span><span>3,940</span><span>3,940</span></div>
    <div class="r"><span>Lender B</span><span></span><span></span><span></span><span></span><span>8,194</span><span>8,194</span><span>8,194</span><span>8,194</span><span>8,194</span></div>
    <div class="r"><span>Equity</span><span></span><span></span><span></span><span></span><span>31,258</span><span>31,258</span><span>31,258</span><span>31,258</span><span>31,258</span></div>
    <div class="r"><span>Lender C</span><span></span><span></span><span></span><span></span><span>20,690</span><span>20,690</span><span>20,690</span><span>20,690</span><span>20,690</span></div>
    <div class="r"><span>Lender D</span><span></span><span></span><span></span><span></span><span>32,743</span><span>32,743</span><span>32,743</span><span>32,743</span><span>32,743</span></div>
    <div class="r"><span>Lender E</span><span></span><span></span><span></span><span></span><span>6,355</span><span>6,355</span><span>6,355</span><span>6,355</span><span>6,355</span></div>
    <div class="r"><span>Lender F</span><span></span><span></span><span></span><span></span><span></span><span></span><span></span><span></span><span></span><span>40,000</span><span>40,000</span><span>40,000</span><span>40,000</span></div>
    <div class="r b"><span></span><span>$0</span><span>$0</span><span>$0</span><span>$0</span><span>103,180</span><span>103,180</span><span>103,180</span><span>103,180</span><span>103,180</span><span>40,000</span><span>40,000</span><span>40,000</span><span>40,000</span></div>
    <div class="r net" style="line-height:5.5px;margin-top:1px"><span>Cash, End of Period</span><span>$0</span><span>$0</span><span>$0</span><span>$1,229,940</span><span>$1,296,340</span><span>$1,374,465</span><span>$1,454,673</span><span>$1,537,415</span><span>$1,616,551</span><span>$1,719,569</span><span>$1,775,327</span><span>$1,801,176</span><span>$1,840,103</span></div>
  </div>
  <div class="note">Model excludes PPP &amp; ERC</div>
  <div class="foot"><b>10</b></div>
</section>

<!-- 11 current cash holding -->
<section class="slide" style="left:323px;top:612px">
  <svg class="ph" viewBox="0 0 314 176" role="img" aria-label="Photo of a smiling crew member in a red shirt serving food">
    <defs><linearGradient id="gp" x1="0" y1="0" x2="1" y2="1"><stop offset="0" stop-color="#6b4a38"/><stop offset=".5" stop-color="#c9483c"/><stop offset="1" stop-color="#e8ddd4"/></linearGradient></defs>
    <polygon points="240,0 314,0 314,176 140,176" fill="url(#gp)"/>
  </svg>
  <div class="logo" style="left:12px;right:auto"><i></i>RBT</div>
  <h2 class="h2" style="left:20px;top:47px"><span class="lt" style="font-weight:700">Current</span> Cash Holding</h2>
  <div class="body" style="left:22px;top:67px">
    <div class="sub">Current Cash as of 8/25/21</div>
    <ul style="margin-left:4px">
      <li>Harbor National Bank</li>
      <li class="in"> Checking: $1,532,893</li>
      <li>Summit Ridge Bank</li>
      <li class="in"> Money Market: $931,358</li>
      <li class="in"> RBT DC Checking: $99,934</li>
      <li>Total Cash: $2,564,190</li>
      <li>2020 ERC Credit: $1,053,536</li>
      <li class="in"> Anticipated Deposit: Q1-22</li>
      <li>2021 ERC under review</li>
    </ul>
  </div>
</section>

<!-- 12 calloway -->
<section class="slide" style="left:643px;top:612px">
  <svg class="ph" viewBox="0 0 314 176" role="img" aria-label="Photo of a restaurant storefront with red awning">
    <defs><linearGradient id="gs" x1="0" y1="0" x2="0" y2="1"><stop offset="0" stop-color="#3b86c3"/><stop offset=".4" stop-color="#d2c1ad"/><stop offset=".6" stop-color="#b8312c"/><stop offset="1" stop-color="#6d6660"/></linearGradient></defs>
    <polygon points="132,0 314,0 314,176 190,176" fill="url(#gs)"/>
    <polygon points="314,40 314,176 232,176" fill="#1f7fb6" opacity=".85"/>
  </svg>
  <div class="logo" style="left:12px;right:auto"><i></i>RBT</div>
  <div class="big" style="left:16px;top:50px">Calloway</div>
  <ul class="facts" style="left:16px;top:74px;line-height:16px">
    <li>At PSA Phase to Sell</li>
    <li>Sales Price: <b>$1.1M</b></li>
    <li>Current Debt: <b>$89k</b></li>
    <li>Target Date: <b>10/6/21</b></li>
    <li style="font-size:4.6px">Approved by Fenwick's Corp</li>
  </ul>
  <div class="caption" style="left:253px;top:158px">Fenwick's Calloway</div>
</section>

<!-- 13 sand hill -->
<section class="slide" style="left:3px;top:812px">
  <h1 class="title"><span class="lt">Sand Hill</span> – Colorado Springs, CO</h1>
  <div class="logo"><i></i>RBT</div>
  <div role="img" aria-label="Aerial site map of the retail center with parcel markings" style="position:absolute;left:110px;top:43px;width:198px;height:106px;background:linear-gradient(135deg,#7a6a5e,#8f7f73 45%,#6f6d5c)"></div>
  <div class="lead" style="left:12px;top:72px;color:#333">2,600 <span style="font-size:4.4px">sqft End-Cap with Drive-Thru</span></div>
  <ul class="mini" style="left:14px;top:80px">
    <li>Total Project Est.: $950k</li>
    <li>Funded debt: $635k</li>
    <li>Equity: $160k</li>
    <li>Soft Cost Cash: $155k</li>
    <li>TI Return: $99k</li>
  </ul>
  <div class="tag" style="left:72px;top:139px;background:#45a29a;font-size:4px">Projected opening Qtr. 2, 2022</div>
  <div class="foot"><b>13</b></div>
</section>

<!-- 14 falcon -->
<section class="slide" style="left:323px;top:812px">
  <h1 class="title"><span class="lt">Falcon</span> – Falcon, CO</h1>
  <div class="logo"><i></i>RBT</div>
  <div role="img" aria-label="Site plan drawing of the shopping center and property" style="position:absolute;left:8px;top:34px;width:125px;height:120px;background:#f1f1f3;border:1px solid #cfcfe0"></div>
  <div class="tag" style="left:2px;top:146px;background:#45a29a;font-size:4px">Projected opening Qtr. 3, 2022</div>
  <div class="banner" style="left:132px;top:34px;width:162px">PSA to acquire .78 acr &amp; construct 3030 sqft bldg.</div>
  <div class="colhead" style="left:143px;top:54px">Real Estate</div>
  <ul class="mini" style="left:143px;top:61px">
    <li>Total Investment: <b>$1.025M</b></li>
    <li>Purchase Price: <b>$1M</b></li>
    <li>Soft Cost: <b>$25k</b></li>
    <li>Funded Debt: <b>$800k</b></li>
    <li>Equity: <b>$200k</b></li>
  </ul>
  <div class="colhead" style="left:143px;top:107px">RE Development</div>
  <ul class="mini" style="left:143px;top:114px">
    <li>Total Investment: <b>$500</b></li>
    <li>Funded Debt: <b>$400k</b></li>
    <li>Equity: <b>$100k</b></li>
  </ul>
  <div class="colhead" style="left:232px;top:54px">Fenwick's</div>
  <ul class="mini" style="left:232px;top:61px">
    <li>Total Investment: <b>$1.1M</b></li>
    <li>Funded Debt: <b>$758k</b></li>
    <li>Equity: <b>$188k</b></li>
    <li>Soft Cost: <b>$157k</b></li>
  </ul>
  <div class="foot"><b>14</b></div>
</section>

<!-- 15 real estate partner -->
<section class="slide" style="left:643px;top:812px">
  <h1 class="title"><span class="lt">Real Estate</span> Partner</h1>
  <div class="logo"><i></i>RBT</div>
  <div style="position:absolute;left:0;top:56px;width:314px;height:70px;box-shadow:0 2px 6px rgba(0,0,0,.08)"></div>
  <div class="partner"><i></i><span>ARBOR<br>LANE<br>PARTNERS</span></div>
  <ul class="checks">
    <li><svg viewBox="0 0 10 10"><circle cx="5" cy="5" r="5" fill="#1f6fa6"/><path d="M2.5 5.2l1.8 1.8 3.4-3.6" fill="none" stroke="#fff" stroke-width="1.2"/></svg>Source &amp; fund opportunities</li>
    <li><svg viewBox="0 0 10 10"><circle cx="5" cy="5" r="5" fill="#1f6fa6"/><path d="M2.5 5.2l1.8 1.8 3.4-3.6" fill="none" stroke="#fff" stroke-width="1.2"/></svg>Manage development process</li>
    <li><svg viewBox="0 0 10 10"><circle cx="5" cy="5" r="5" fill="#1f6fa6"/><path d="M2.5 5.2l1.8 1.8 3.4-3.6" fill="none" stroke="#fff" stroke-width="1.2"/></svg>Turn over a turn key Fenwick's</li>
    <li><svg viewBox="0 0 10 10"><circle cx="5" cy="5" r="5" fill="#1f6fa6"/><path d="M2.5 5.2l1.8 1.8 3.4-3.6" fill="none" stroke="#fff" stroke-width="1.2"/></svg>Reduce capital needs to FFE</li>
    <li><svg viewBox="0 0 10 10"><circle cx="5" cy="5" r="5" fill="#1f6fa6"/><path d="M2.5 5.2l1.8 1.8 3.4-3.6" fill="none" stroke="#fff" stroke-width="1.2"/></svg>Able to finance debt in lease over 20 yrs</li>
    <li><svg viewBox="0 0 10 10"><circle cx="5" cy="5" r="5" fill="#1f6fa6"/><path d="M2.5 5.2l1.8 1.8 3.4-3.6" fill="none" stroke="#fff" stroke-width="1.2"/></svg>Faster pace of development than internal</li>
  </ul>
  <div class="foot"><b>15</b></div>
</section>

<!-- 16 calendar -->
<section class="slide" style="left:3px;top:1012px">
  <h1 class="title"><span class="lt" style="font-weight:700">Calendar</span></h1>
  <div class="logo"><i></i>RBT</div>
  <svg viewBox="0 0 314 176" style="position:absolute;left:0;top:0;width:314px;height:176px">
    <rect x="42" y="83" width="232" height="16" rx="8" fill="#c9cdd0"/>
    <rect x="42" y="83" width="170" height="16" rx="8" fill="#3aa0c2"/>
    <rect x="95" y="83" width="60" height="16" fill="#5aa7a0"/>
    <g fill="#fff" stroke="#2a8fc6" stroke-width="1.6">
      <circle cx="52" cy="91" r="8"/><circle cx="102" cy="91" r="8"/><circle cx="152" cy="91" r="8"/><circle cx="202" cy="91" r="8"/>
    </g>
    <g fill="none" stroke="#555" stroke-width=".7">
      <rect x="48.5" y="87.5" width="7" height="7" rx=".6"/><path d="M50 90h4M50 92h3"/>
      <path d="M98 95h8M99 94v-2M102 94v-4M105 94v-3"/>
      <circle cx="152" cy="91" r="3.2"/><circle cx="152" cy="91" r="1"/>
      <path d="M198.5 89.5h2.5l3-2v7l-3-2h-2.5z"/>
    </g>
    <g stroke="#999" stroke-width=".4"><line x1="52" y1="69" x2="52" y2="83"/><line x1="102" y1="99" x2="102" y2="113"/><line x1="152" y1="69" x2="152" y2="83"/><line x1="202" y1="99" x2="202" y2="113"/></g>
    <g fill="#fff" stroke="#999" stroke-width=".4"><circle cx="52" cy="69" r="1.2"/><circle cx="102" cy="113" r="1.2"/><circle cx="152" cy="69" r="1.2"/><circle cx="202" cy="113" r="1.2"/></g>
  </svg>
  <div class="cal" style="left:55px;top:57px">End of October<b class="t">Tax Planning Meeting</b></div>
  <div class="cal" style="left:155px;top:57px">October 20th, 2021<b>Quarter 3 Meeting Date<br>(Qtr 3 ends 9/8/21)</b></div>
  <div class="cal" style="left:105px;top:110px">End of November<b>2022 Budgeting</b></div>
  <div class="cal" style="left:205px;top:110px">October 6, 2021<b>RBT Double Cheese<br>Internal Announcement</b></div>
  <div class="foot"><b>16</b></div>
</section>

<!-- 17 florida -->
<section class="slide" style="left:323px;top:1012px">
  <h1 class="title"><span class="lt">Florida</span> Development Plan</h1>
  <div class="logo"><i></i>RBT</div>
  <div role="img" aria-label="Map of northeast Florida with restaurant location pins" style="position:absolute;left:8px;top:32px;width:157px;height:138px;background:linear-gradient(100deg,#e6ece3 0%,#dfe7dc 75%,#a9d3e6 88%,#8ec7e0 100%)"></div>
  <div class="fl">Fleming Island<em>Under Review</em>Durbin Creek – LOI<em>Target: Q3-23</em>Yulee – LOI<em>Target: Q3 - 23</em></div>
  <div class="foot"><b>17</b></div>
</section>

<!-- 18 questions -->
<section class="slide" style="left:643px;top:1012px">
  <div class="ph" role="img" aria-label="Dusk photo of a restaurant exterior with a flag" style="background:linear-gradient(180deg,#5f6a70 0%,#3d4346 60%,#2a2d2e 100%)"></div>
  <div class="qbox">
    <div class="mark">RBT</div>
    <div class="q">Questions?</div>
  </div>
</section>

</body>
</html>
```